Heron Accord Business Card

Need a business card for my nonprofit, Heron Accord Inc. Heron Accord is a conflict resolution practice that offers services that help people resolve problems peacefully.

Got Conflict? Try Conflict Coaching. Initial consultation is complimentary

Marisol Daventry-Kuhl, PhD
Heron Accord Inc.
www.heronaccord-example.org
E: info@heronaccord-example.org
P: 555-318-4927

Would like the attached logo on it, as well as our slogan, which is Finding Calm Around the RoomĀ®

```html
<!DOCTYPE html>
<html lang="en">
<head>
<meta charset="utf-8">
<title>Heron Accord Business Card</title>
<link rel="stylesheet" href="https://fonts.googleapis.com/css2?family=Arimo&family=Crimson+Text&family=Jost:wght@400&display=swap">
<style>
  :root {
    --backdrop: #eceeed;
    --card: #ffffff;
    --petal-red: #e0202a;
    --petal-deep: #c4141e;
    --petal-light: #ee4a4e;
    --accent-red: #e8323a;
    --gold-dark: #b0862a;
    --gold-mid: #e2bc52;
    --gold-light: #f6dc86;
    --ink: #2a2a2a;
    --slogan-ink: #4a3a14;
  }
  * { margin: 0; padding: 0; box-sizing: border-box; }
  html, body { width: 1200px; height: 900px; overflow: hidden; }
  body { background: var(--backdrop); position: relative; }

  .card {
    position: absolute;
    top: 300px;
    width: 516px;
    height: 298px;
    border-radius: 22px;
    background: var(--card);
    overflow: hidden;
    box-shadow: 0 1px 4px rgba(0,0,0,0.18);
  }
  .card--front { left: 71px; }
  .card--back { left: 615px; }

  .front-artwork {
    position: absolute;
    inset: 0;
    background: linear-gradient(180deg, var(--petal-deep) 0%, var(--petal-red) 55%, var(--petal-light) 100%);
  }

  .brand-name {
    position: absolute;
    top: 52px;
    left: 0;
    width: 100%;
    text-align: center;
    font-family: "Jost", sans-serif;
    font-weight: 400;
    font-size: 40px;
    letter-spacing: 3px;
    color: var(--gold-dark);
    text-transform: uppercase;
  }

  .pitch {
    position: absolute;
    left: 41px;
    top: 201px;
    font-family: "Arimo", sans-serif;
    font-size: 21px;
    line-height: 27px;
    color: var(--accent-red);
  }

  .contact {
    position: absolute;
    left: 292px;
    top: 166px;
    font-family: "Crimson Text", serif;
    color: var(--ink);
  }
  .contact__name { font-size: 15px; margin-bottom: 7px; }
  .contact__list { list-style: none; font-size: 14px; line-height: 20px; }
  .contact__list li { display: flex; align-items: center; gap: 6px; }
  .contact__icon { width: 11px; height: 11px; flex: none; }

  .slogan-band {
    position: absolute;
    left: 0;
    bottom: 0;
    width: 100%;
    height: 34px;
    background: linear-gradient(90deg, var(--gold-dark) 0%, var(--gold-mid) 35%, var(--gold-light) 55%, var(--gold-mid) 75%, var(--gold-dark) 100%);
    display: flex;
    align-items: center;
    justify-content: center;
    font-family: "Crimson Text", serif;
    font-size: 13px;
    letter-spacing: 7px;
    text-transform: uppercase;
    color: var(--slogan-ink);
  }
</style>
</head>
<body>
  <section class="card card--front">
    <div class="front-artwork" role="img" aria-label="Photograph of red flower petals opening upward"></div>
  </section>

  <section class="card card--back">
    <div class="brand-name">Heron Accord</div>

    <p class="pitch">Got conflict?<br>Try conflict coaching</p>

    <div class="contact">
      <p class="contact__name">Marisol Daventry-Kuhl, PhD</p>
      <ul class="contact__list">
        <li>
          <svg class="contact__icon" viewBox="0 0 12 12" aria-hidden="true"><circle cx="6" cy="6" r="6" fill="#e8323a"/><path d="M3.4 4.2c.2 1.9 2.4 4.1 4.4 4.4l.8-.9-1.1-.8-.6.5C6 7 5 6 4.6 5.1l.5-.6-.8-1.1z" fill="#fff"/></svg>
          555-318-4927
        </li>
        <li>
          <svg class="contact__icon" viewBox="0 0 12 12" aria-hidden="true"><circle cx="6" cy="6" r="6" fill="#e8323a"/><rect x="3" y="4" width="6" height="4.2" fill="#fff"/><path d="M3 4l3 2.3L9 4" stroke="#e8323a" stroke-width="0.7" fill="none"/></svg>
          info@heronaccord-example.org
        </li>
        <li>
          <svg class="contact__icon" viewBox="0 0 12 12" aria-hidden="true"><circle cx="6" cy="6" r="6" fill="#e8323a"/><circle cx="6" cy="6" r="3" stroke="#fff" stroke-width="0.8" fill="none"/><path d="M3 6h6M6 3c-1.2 1.6-1.2 4.4 0 6M6 3c1.2 1.6 1.2 4.4 0 6" stroke="#fff" stroke-width="0.6" fill="none"/></svg>
          www.heronaccord-example.org
        </li>
      </ul>
    </div>

    <div class="slogan-band">Finding Calm Around the Room®</div>
  </section>
</body>
</html>
```